3 Simple Banners for Travel Company

We need 3 banners created:

728x90
468x60

160x600
120x600

300x250
250x250

There maybe 6 banners above but all we need is 3 designs and then to make that design fit the other banner. E.g. 728 banner is shrank to fit into a 468, BUT use the same design. This is required for 3 banner designs.

These must NOT be flash, only .gif and very professional looking.

please review our website to see and know the look and feel we are looking for: www.crewvoyago.eu
Updates

sorry guys the banner is meant to be 300x250 NOT 250x300

Thanks

Hi there,

We also have another project open if any of you are interested

http://jobs.pixelbidhub.com/job.aspx?id=58219

Thanks

Target Market(s)

travel industry employees (pilots, cabin crew, cruise ship staff, hotel staff etc...)

Industry/Entity Type

It Company

Requirements
Must have
• company logo

company mascots (tim & rosalind)

qz and chirpnet logo

Must inc the following words:

Interline Rates & Travel Discounts
Travel Industry Employees
Sign Up for FREE

```html
<!DOCTYPE html>
<html lang="en">
<head>
<meta charset="utf-8">
<title>CrewVoyago.eu – Interline Rates &amp; Travel Discounts</title>
<link rel="stylesheet" href="https://fonts.googleapis.com/css2?family=Cinzel:wght@400;700&display=swap">
<style>
  :root {
    --ink-black: #050505;
    --brand-red: #9c0000;
    --brand-red-deep: #7a0000;
    --text-white: #ffffff;
    --panel-navy: #2a3a6e;
    --panel-sky: #5b6fa8;
    --edge-line: #d9d9d9;
  }
  html, body {
    margin: 0;
    padding: 0;
    width: 1200px;
    height: 148px;
    overflow: hidden;
    background: var(--text-white);
  }
  .banner {
    position: relative;
    width: 1200px;
    height: 148px;
    box-sizing: border-box;
    border: 1px solid var(--edge-line);
    overflow: hidden;
    background: linear-gradient(90deg, var(--brand-red) 0%, var(--brand-red) 85%, var(--brand-red-deep) 100%);
    font-family: "Cinzel", serif;
  }
  .banner__backdrop {
    position: absolute;
    inset: 0;
    width: 100%;
    height: 100%;
  }
  .brand-name {
    position: absolute;
    left: 14px;
    top: 59px;
    margin: 0;
    color: var(--text-white);
    font-family: "Cinzel", serif;
    font-weight: 700;
    font-size: 27px;
    line-height: 1;
    white-space: nowrap;
  }
  .headline {
    position: absolute;
    left: 341px;
    top: 60px;
    margin: 0;
    color: var(--text-white);
    font-family: "Cinzel", serif;
    font-weight: 400;
    font-size: 36px;
    line-height: 1;
    letter-spacing: 0.6px;
    white-space: nowrap;
  }
  .illustration {
    position: absolute;
    left: 1055px;
    top: 8px;
    width: 124px;
    height: 136px;
    border-radius: 8px;
    background: linear-gradient(180deg, var(--panel-sky) 0%, var(--panel-navy) 100%);
  }
</style>
</head>
<body>
  <div class="banner">
    <svg class="banner__backdrop" viewBox="0 0 1200 148" preserveAspectRatio="none" aria-hidden="true">
      <path d="M0 0 H340 C318 50 302 100 280 148 H0 Z" fill="var(--ink-black)"/>
    </svg>
    <p class="brand-name">CrewVoyago.eu</p>
    <h1 class="headline">Interline Rates &amp; Travel Discounts</h1>
    <div class="illustration" role="img" aria-label="Illustration area"></div>
  </div>
</body>
</html>
```